Get referrals for Insurance customers and the domain name is tallyfinch.ca We are an insurance

We need a logo and a website for a referral site. Our advertising and promotion will send customers to this website where they will fill out a form giving their information as well as person they want to refer. The logo idea that I have is a gear with a dollar sign in it the number 2 and the letter U. Another words dollars to you. If this can be animated with sounds, that would be great. Once this form is filled in it goes to a referral software site such as Lantern Quay or Bonusvale where the data is saved for us to follow up. This is not a complicated site. It will reassure the people who will refer their friends, family members or other aquiatnces that we will provide great service to and best prices for home and business insurance. It will exclude auto insurance as not referral for a monitory reward(regulations). The reward will be $100 for business and house insurance and $25 condo or townhome insurance. It will imply that this $100 is limited time offer. The site should be set so that we could edit the website once the designer has given it to us. The people we expecting to be our referrers are real estate agents, notaries public, and our existing customers.
Updates

The designs are not what I was expecting. Is there any way I can communicate with the designer that I think made the best attempt at what I was expecting?

Target Market(s)

Our customers, realtors, notaries public and anyone who knows

Industry/Entity Type

Insurance Broker

Logo Text

Dollar sign, Gear, number 2 and U a funnel. Dollars to you . See what you can

Number of Pages Required

4 page

Font styles to use
Other font styles liked:
• Calibri

Colors
0455a3
ec1f27
ffffff

Requirements
Must have
• Fillable form on info about referer and the referred. This will data will be sent to the third party who will have our data for keeping track of the referrals and where Our referees can see how many people they have referred and who has been approved for payment. The third parties our such as Lantern Quay or Bonusvale.
Nice to have
• Animated logo with sound would be nice. This will be used on the website only. We use ashgrove insurance logo as seen on www,ashgroveinsurance.ca for all communications.
Should not have
• I have attached two files for reference only they do not have the exact text that I want to have on the website. I am working on that and it will always be changing to some extent. You can talk to me.

```html
<!DOCTYPE html>
<html lang="en">
<head>
<meta charset="utf-8">
<title>Tallyfinch – Insurance Referrals</title>
<link href="https://fonts.googleapis.com/css2?family=Open+Sans:wght@400;600;700;800&family=Ubuntu:wght@400;500;700&display=swap" rel="stylesheet">
<style>
:root{
  --blue:#0455a3;
  --blue-deep:#0b3f7e;
  --navy:#13243d;
  --red:#ec1f27;
  --white:#ffffff;
  --ink:#1d1d1d;
  --grey:#5a5a5a;
  --pale:#eef2f7;
  --footer:#222428;
}
*{margin:0;padding:0;box-sizing:border-box}
html,body{width:1200px;height:3579px;overflow:hidden;background:var(--white)}
body{position:relative;font-family:"Open Sans",Arial,sans-serif;color:var(--ink)}
.abs{position:absolute}
.heading{font-family:"Ubuntu",Arial,sans-serif}

/* top bar */
.topbar{left:0;top:0;width:1200px;height:38px;border-bottom:1px solid #e6e6e6;font-size:13px;color:#333}
.topbar .phone{left:120px;top:10px;display:flex;align-items:center;gap:8px}
.topbar .mail{left:532px;top:10px;display:flex;align-items:center;gap:8px}
.social{display:flex;gap:8px}
.social span{width:20px;height:20px;border-radius:50%;background:#555;display:block}
.topbar .social{right:108px;top:9px}

/* header */
.header{left:0;top:38px;width:1200px;height:153px}
.logo{left:122px;top:40px;display:flex;align-items:center;gap:14px}
.logo .mark{width:70px;height:70px;border-radius:50%;background:var(--blue)}
.logo .name{font-family:"Ubuntu",sans-serif;font-weight:700;font-size:40px;color:var(--blue)}
.nav{left:492px;top:76px;display:flex;gap:38px;font-size:16px;font-weight:700;letter-spacing:.3px}
.nav a{color:var(--ink);text-decoration:none;position:relative}
.nav a.active::after{content:"";position:absolute;left:0;right:0;top:28px;height:4px;background:var(--red)}
.nav .caret{font-size:11px}

/* hero */
.hero{left:0;top:191px;width:1200px;height:489px;background:linear-gradient(90deg,#1a2536 0%,#243349 45%,#3a4a60 70%,#2b384c 100%)}
.hero .photo{right:0;top:0;width:560px;height:489px;background:radial-gradient(circle at 55% 60%,#6f7d90 0%,#3b495c 45%,#202c3d 80%)}
.hero h1{left:120px;top:180px;font-size:44px;font-weight:800;color:var(--white);letter-spacing:1px}
.hero p{left:120px;top:236px;width:340px;font-size:14px;line-height:18px;color:var(--white)}
.btn{background:var(--red);color:var(--white);font-size:12px;font-weight:700;display:flex;align-items:center;justify-content:center}
.hero .btn{left:124px;top:305px;width:122px;height:31px}
.arrow-side{top:220px;width:40px;height:60px}
.quote{left:117px;top:379px;width:961px;height:110px;background:rgba(4,85,163,.92)}
.field{top:36px;height:34px;background:var(--white);font-size:12px;color:#555;padding:0 10px;display:flex;align-items:center;justify-content:space-between}
.quote .btn{left:770px;top:36px;width:162px;height:34px;font-size:13px}

.dots{display:flex;gap:16px}
.dots span{width:18px;height:18px;border-radius:50%;background:#c7ccd6}
.dots span.on{background:var(--blue)}
.dots.red span.on{background:#b5161d}

/* features */
.features{left:0;top:680px;width:1200px;height:363px}
.feature{top:79px;width:220px}
.feature svg{display:block}
.feature h3{margin-top:22px;font-size:19px;line-height:22px;font-weight:700;color:var(--ink)}
.feature p{margin-top:8px;font-size:14px;line-height:18px;color:#333}
.feature .more{margin-top:10px;font-size:14px;font-weight:700;display:flex;align-items:center;gap:8px}

/* protection band */
.band{left:0;top:1043px;width:1200px;height:389px;background:var(--pale)}
.band .photo{left:602px;top:0;width:598px;height:389px;background:linear-gradient(135deg,#0f3e73 0%,#1f6fb8 45%,#0a2f5c 100%)}
.band h2{left:120px;top:88px;font-size:22px;line-height:28px;color:var(--blue);font-weight:500}
.drop{left:119px;width:415px;height:29px;background:var(--red);color:var(--white);font-size:14px;padding:0 12px;display:flex;align-items:center;justify-content:space-between}

/* talking */
.talk h2{left:0;width:1200px;top:1524px;text-align:center;font-size:36px;font-weight:500}
.talk .rule{left:556px;top:1574px;width:88px;height:3px;background:var(--ink)}
.talk p{left:120px;top:1604px;width:955px;text-align:center;font-size:14px;line-height:19px;color:#222}
.talk .btn{left:544px;top:1739px;width:122px;height:31px}

/* chances */
.chances{left:0;top:1861px;width:1200px;height:489px;background:linear-gradient(180deg,#1d5fa8 0%,#2a6cb5 50%,#1b579c 100%)}
.chances h2{left:0;width:1200px;top:18px;text-align:center;color:var(--white);font-size:32px;font-weight:400}
.card{top:67px;height:374px;background:var(--white);border-radius:6px;overflow:hidden;box-shadow:0 2px 6px rgba(0,0,0,.3)}
.card .cap{height:43px;background:var(--red);color:var(--white);font-family:"Ubuntu",sans-serif;font-weight:700;font-size:24px;display:flex;align-items:center;justify-content:center}
.card .sub{height:32px;background:#e8edf5;color:var(--blue);font-size:14px;font-weight:700;padding:0 18px;display:flex;align-items:center}
.card ul{padding:14px 18px 0 40px;font-size:14px;line-height:34px}
.card .txt{padding:14px 18px 0;font-size:14px;line-height:34px}
.card .img{position:absolute;left:40px;right:40px;bottom:32px;height:100px;border-radius:4px}

/* testimonials */
.tt-small{left:0;width:1200px;top:2424px;text-align:center;font-size:16px;color:#444;letter-spacing:1px}
.tt-title{left:0;width:1200px;top:2452px;text-align:center;font-size:30px;font-weight:500;letter-spacing:1.5px}
.tcard{top:2613px;height:202px;border:1px solid #ececec;background:var(--white);text-align:center}
.tcard .who{margin-top:-3px;padding-top:10px}
.avatar{width:90px;height:90px;border-radius:50%;background:radial-gradient(circle,#c9b8a6,#7d6a5b);border:3px solid #fff;box-shadow:0 0 0 1px #ddd}
.tname{top:2627px;font-size:14px;font-weight:700;text-align:center}
.trole{top:2648px;font-size:13px;color:#555;text-align:center}
.tquote{top:2700px;font-size:14px;line-height:20px;color:#555;text-align:center}

/* newsletter */
.news{left:0;top:2935px;width:1200px;height:238px;background:var(--blue)}
.news h2{left:0;width:1200px;top:44px;text-align:center;color:var(--white);font-size:30px;font-weight:400;letter-spacing:3px}
.news p{left:0;width:1200px;top:84px;text-align:center;color:var(--white);font-size:17px;letter-spacing:2px}
.news .input{left:339px;top:126px;width:549px;height:36px;background:var(--white);font-size:11px;color:#777;padding:0 18px;display:flex;align-items:center}
.news .btn{left:787px;top:132px;width:96px;height:24px;font-size:14px;letter-spacing:1px}

/* contact */
.contact{left:0;top:3173px;width:1200px;height:351px;background:linear-gradient(180deg,#f3f5f8,#e9edf2)}
.contact h2{left:0;width:1200px;top:42px;text-align:center;font-size:30px;font-weight:500;letter-spacing:2px}
.cinfo{top:110px;width:300px;text-align:center}
.cinfo .ico{width:82px;height:82px;border-radius:50%;background:var(--red);margin:0 auto;display:flex;align-items:center;justify-content:center}
.cinfo h4{margin-top:26px;font-size:17px;font-weight:600;letter-spacing:2px;color:#222}
.cinfo div.v{margin-top:6px;font-size:19px;color:#333;line-height:24px}

/* footer */
.footer{left:0;top:3524px;width:1200px;height:55px;background:var(--footer);color:var(--white)}
.footer .links{left:120px;top:18px;font-size:13px;font-weight:700;letter-spacing:.5px}
.footer .social{right:108px;top:15px;gap:14px}
.footer .social span{width:27px;height:27px;background:#e8e8e8}
</style>
</head>
<body>

<div class="abs topbar">
  <div class="abs phone">
    <svg width="14" height="14" viewBox="0 0 24 24"><path d="M6.6 10.8a15 15 0 006.6 6.6l2.2-2.2c.3-.3.7-.4 1-.2 1.1.4 2.3.6 3.6.6.6 0 1 .4 1 1V20c0 .6-.4 1-1 1A17 17 0 013 4c0-.6.4-1 1-1h3.5c.6 0 1 .4 1 1 0 1.3.2 2.5.6 3.6.1.3 0 .7-.2 1z" fill="#333"/></svg>
    <span>604-555-0148</span>
  </div>
  <div class="abs mail">
    <svg width="16" height="12" viewBox="0 0 16 12"><rect width="16" height="12" fill="#333"/><path d="M0 0l8 6 8-6" stroke="#fff" fill="none" stroke-width="1.3"/></svg>
    <span>info@ashgroveinsurance.ca</span>
  </div>
  <div class="abs social"><span></span><span></span><span></span><span></span><span></span></div>
</div>

<header class="abs header">
  <div class="abs logo"><div class="mark"></div><div class="name">Tallyfinch</div></div>
  <nav class="abs nav">
    <a class="active">HOME</a><a>ABOUT</a><a>SERVICES <span class="caret">▼</span></a><a>BLOG</a><a>TESTMONIAL</a><a>CONTACTS</a>
  </nav>
</header>

<section class="abs hero">
  <div class="abs photo" role="img" aria-label="Businessman cupping a small glowing house in his hands"></div>
  <svg class="abs arrow-side" style="left:40px" viewBox="0 0 40 60"><path d="M28 10L10 30l18 20" stroke="rgba(255,255,255,.35)" stroke-width="6" fill="none"/></svg>
  <svg class="abs arrow-side" style="right:40px" viewBox="0 0 40 60"><path d="M12 10l18 20-18 20" stroke="rgba(255,255,255,.35)" stroke-width="6" fill="none"/></svg>
  <h1 class="abs">TALLYFINCH</h1>
  <p class="abs">Lorem Ipsum is simply dummy text of the print and typesetting Lorem Ipsum has been the industry's standard.</p>
  <div class="abs btn">Read More</div>
  <form class="abs quote">
    <div class="abs field" style="left:38px;width:166px">Name</div>
    <div class="abs field" style="left:222px;width:166px">Email</div>
    <div class="abs field" style="left:406px;width:166px">Phone <span>⬍</span></div>
    <div class="abs field" style="left:590px;width:166px">Types of Insurance <span>⬍</span></div>
    <div class="abs btn">Get Secure Quote</div>
  </form>
</section>

<div class="abs dots" style="left:551px;top:700px"><span></span><span class="on"></span><span></span></div>

<section class="abs features">
  <div class="abs feature" style="left:122px">
    <svg width="62" height="64" viewBox="0 0 62 64"><path d="M14 6h34v18c0 10-8 16-17 19C22 40 14 34 14 24z" fill="var(--blue)"/><path d="M22 22l7 7 12-13" stroke="#fff" stroke-width="4" fill="none"/><path d="M4 50c10-6 20-6 30 0h18v8H4z" fill="var(--blue)"/></svg>
    <h3>Assuring Proper Coverage</h3>
    <p>Lorem Ipsum is simply printing and industry.</p>
    <div class="more">Read More.. <svg width="18" height="18" viewBox="0 0 18 18"><circle cx="9" cy="9" r="8" stroke="#222" stroke-width="1.5" fill="none"/><path d="M7 5l4 4-4 4" stroke="#222" stroke-width="1.5" fill="none"/></svg></div>
  </div>
  <div class="abs feature" style="left:406px">
    <svg width="62" height="64" viewBox="0 0 62 64"><circle cx="31" cy="22" r="14" fill="var(--blue)"/><path d="M14 22a17 17 0 0134 0" stroke="var(--blue)" stroke-width="4" fill="none"/><path d="M6 62c2-16 12-22 25-22s23 6 25 22z" fill="var(--blue)"/></svg>
    <h3>Providing Excellent Customer</h3>
    <p>Lorem Ipsum is simply printing and industry.</p>
    <div class="more">Read More.. <svg width="18" height="18" viewBox="0 0 18 18"><circle cx="9" cy="9" r="8" stroke="#222" stroke-width="1.5" fill="none"/><path d="M7 5l4 4-4 4" stroke="#222" stroke-width="1.5" fill="none"/></svg></div>
  </div>
  <div class="abs feature" style="left:670px">
    <svg width="62" height="64" viewBox="0 0 62 64"><path d="M18 38l-8 22 10-4 6 8 5-20zM44 38l8 22-10-4-6 8-5-20z" fill="var(--blue)"/><circle cx="31" cy="24" r="20" fill="var(--blue)"/><path d="M31 12l3.5 7.5 8 1-6 5.5 1.5 8L31 30l-7 4 1.5-8-6-5.5 8-1z" fill="#fff"/></svg>
    <h3>Obtaining Lowest Premium</h3>
    <p>Lorem Ipsum is simply printing and industry.</p>
    <div class="more">Read More.. <svg width="18" height="18" viewBox="0 0 18 18"><circle cx="9" cy="9" r="8" stroke="#222" stroke-width="1.5" fill="none"/><path d="M7 5l4 4-4 4" stroke="#222" stroke-width="1.5" fill="none"/></svg></div>
  </div>
  <div class="abs feature" style="left:933px">
    <svg width="62" height="64" viewBox="0 0 62 64"><rect x="12" y="4" width="36" height="56" rx="6" stroke="var(--blue)" stroke-width="4" fill="none"/><circle cx="34" cy="26" r="12" stroke="var(--blue)" stroke-width="3" fill="none"/><text x="34" y="30" font-size="11" font-weight="700" text-anchor="middle" fill="var(--blue)" font-family="Open Sans,sans-serif">24</text></svg>
    <h3>Offering Free Mobile service</h3>
    <p>Lorem Ipsum is simply printing and industry.</p>
    <div class="more">Read More.. <svg width="18" height="18" viewBox="0 0 18 18"><circle cx="9" cy="9" r="8" stroke="#222" stroke-width="1.5" fill="none"/><path d="M7 5l4 4-4 4" stroke="#222" stroke-width="1.5" fill="none"/></svg></div>
  </div>
</section>

<section class="abs band">
  <div class="abs photo" role="img" aria-label="Blue tiles with insurance symbols and a large insurance headline"></div>
  <h2 class="abs heading">We will Provide The Best Protection for<br>Your Client's New Investment For</h2>
  <div class="abs drop" style="top:176px">Single Family homes, Townhouse, Condominiums <span>▼</span></div>
  <div class="abs drop" style="top:224px">Rental/Investment properties <span>▼</span></div>
  <div class="abs drop" style="top:272px">Corporate ownership and/or multiple owners <span>▼</span></div>
</section>

<section class="talk">
  <h2 class="abs heading">Just Keep Talking</h2>
  <div class="abs rule"></div>
  <p class="abs">We've built our insurance agency by taking special care of you – and our other clients. And it shows in the large number of people who call us because you recommend us. Naturally we want to grow – but only with the right kind of clients. Clients like you. Our best new clients call us because you recommend us, so... we LOVE it when you "Just KeepTalking"aboutthe specialtreatment &amp; competitive premiums you receive from us! Now, we want to add a little FUN to the process! We're going to make YOU A WINNER when you tell a friend, relative, neighbour or colleague about us at:</p>
  <div class="abs btn">Read More</div>
</section>

<section class="abs chances">
  <h2 class="abs heading">3 Chance For You To Win!</h2>
  <div class="abs card" style="left:119px;width:303px">
    <div class="cap">1st Chance</div>
    <div class="sub">Maple Brew's $5GiftCard</div>
    <ul><li>1 chance to win a $50 GAS CARD<br>(awarded each month)</li><li style="line-height:24px;margin-top:8px">1 chance to winThe GRAND PRIZE 40" Vistara LEDTV*</li></ul>
    <div class="img" role="img" aria-label="Coffee gift card and cup" style="background:linear-gradient(90deg,#6b4a35,#b33a2e)"></div>
  </div>
  <div class="abs card" style="left:449px;width:300px">
    <div class="cap">2ndChance</div>
    <div class="sub">The winner will receive a $50 Gas Card</div>
    <ul style="line-height:30px"><li>The First Week of Each month we;ll randomly draw all of last month;s winners of gift card qualifies</li></ul>
    <div class="img" role="img" aria-label="Fuel nozzle with $50 gas card" style="background:linear-gradient(180deg,#f1f1f1,#d63a2f)"></div>
  </div>
  <div class="abs card" style="left:775px;width:303px">
    <div class="cap">Grand Prize</div>
    <div class="sub" style="height:44px;line-height:18px">The Grand Price Winner will receive a</div>
    <div class="txt">40"VISTARA LEDTV*<br>justin time for the BIG GAME!!!</div>
    <div class="img" role="img" aria-label="Flat screen television" style="background:linear-gradient(180deg,#3c6c9c,#1b2a3a)"></div>
  </div>
</section>

<div class="abs tt-small">Our Testimonials</div>
<div class="abs tt-title heading">What Clients Say About us</div>

<div class="abs tcard" style="left:40px;width:365px"></div>
<div class="abs tcard" style="left:430px;width:370px"></div>
<div class="abs tcard" style="left:823px;width:347px"></div>

<div class="abs avatar" role="img" aria-label="Client portrait" style="left:184px;top:2512px"></div>
<div class="abs avatar" role="img" aria-label="Client portrait" style="left:548px;top:2512px;background:radial-gradient(circle,#9a8a7e,#4d4540)"></div>
<div class="abs avatar" role="img" aria-label="Client portrait" style="left:912px;top:2512px;background:radial-gradient(circle,#a89688,#3a3634)"></div>

<div class="abs tname" style="left:40px;width:365px">Jane Doe</div>
<div class="abs trole" style="left:40px;width:365px">Enginer of Media Production</div>
<div class="abs tquote" style="left:90px;width:265px">Lorem ipsum dolor sit amet, consectetur adipiscing elit. Morbi vel bibendum nullam imperdiet fermentum molestie.</div>

<div class="abs tname" style="left:430px;width:370px">Jane Dolor</div>
<div class="abs trole" style="left:430px;width:370px">Enginer of Media Production</div>
<div class="abs tquote" style="left:480px;width:270px">Lorem ipsum dolor sit amet, consectetur adipiscing elit. Morbi vel bibendum nullam imperdiet fermentum molestie.</div>

<div class="abs tname" style="left:823px;width:347px">John Doe</div>
<div class="abs trole" style="left:823px;width:347px">Enginer of Media Production</div>
<div class="abs tquote" style="left:862px;width:270px">Lorem ipsum dolor sit amet, consectetur adipiscing elit. Morbi vel bibendum nullam imperdiet fermentum molestie.</div>

<div class="abs dots red" style="left:566px;top:2849px"><span></span><span></span><span class="on"></span></div>

<section class="abs news">
  <h2 class="abs">SUBSCRIBE TO OUR NEWSLETTER</h2>
  <p class="abs">TO RECEIVE THE LATEST NEWS &amp; UPDATE</p>
  <div class="abs input">Your E-Mail</div>
  <div class="abs btn">SUBMIT</div>
</section>

<section class="abs contact">
  <h2 class="abs">CONTACT</h2>
  <div class="abs cinfo" style="left:29px">
    <div class="ico"><svg width="38" height="38" viewBox="0 0 24 24"><path d="M6.6 10.8a15 15 0 006.6 6.6l2.2-2.2c.3-.3.7-.4 1-.2 1.1.4 2.3.6 3.6.6.6 0 1 .4 1 1V20c0 .6-.4 1-1 1A17 17 0 013 4c0-.6.4-1 1-1h3.5c.6 0 1 .4 1 1 0 1.3.2 2.5.6 3.6.1.3 0 .7-.2 1z" fill="#fff"/></svg></div>
    <h4>PHONE</h4>
    <div class="v">604-555-0148</div>
  </div>
  <div class="abs cinfo" style="left:451px">
    <div class="ico"><svg width="32" height="42" viewBox="0 0 24 32"><path d="M12 0a12 12 0 00-12 12c0 9 12 20 12 20s12-11 12-20A12 12 0 0012 0z" fill="#fff"/><circle cx="12" cy="12" r="5" fill="var(--red)"/></svg></div>
    <h4>ADDRESS</h4>
    <div class="v">1840 Alder Lane, Brookmere, BC,<br>V0X 1K9</div>
  </div>
  <div class="abs cinfo" style="left:819px">
    <div class="ico"><svg width="40" height="30" viewBox="0 0 16 12"><rect width="16" height="12" rx="1" fill="#fff"/><path d="M0.5 0.8l7.5 5.6 7.5-5.6" stroke="var(--red)" fill="none" stroke-width="1.2"/></svg></div>
    <h4>EMAIL</h4>
    <div class="v">info@ashgroveinsurance.ca</div>
  </div>
</section>

<footer class="abs footer">
  <div class="abs links">PRIVACY POLICY - LEGAL MENTIONS - TERMS AND CONDITIONS</div>
  <div class="abs social"><span></span><span></span><span></span><span></span><span></span></div>
</footer>

</body>
</html>
```